Web Design for Solar Energy Consultancy Company

~ May 3, 2017 Update ~
As our project is rapidly progressing towards its completion, we started building up the list of designs that attracted the most of the team's attention. Additional submittals are still most welcome. Before submitting your proposal, however, we can recommend to review the concepts that received 4 stars as these are the ones that, in our opinion, most closely match the brief's requirements. Thank you!!
~ April 30, 2017 Update ~
The project deadline has been extended to attract a broader design community and to better tailor the final design to the requirements of the project.
A "light", "clean" (minimalistic), professionally looking, unique design is expected. Please, try to avoid industry cliches. Also, please use green, which became another industry cliche, with great caution. The brief provides minimum details to foster creativity. With the same notion in mind, the page content information is not provided.
Thank you for your feedback and support of the project!!
~ April 22, 2017 Update ~
Additional comments after starting receiving more designs:
- your attention to the brief's requirements will be highly appreciated. It is expected that the design is unique - standard, commonly used, images, formats and approaches do not fall under this category. There is no need to "bombard" with slightly different variations of the same design. It is expected that a conceptual (preliminary) design is submitted first, and, after it is reviewed (each design will receive a star rating and, if the star rating is greater than 3, a detailed feedback), the requested changes are implemented. We believe this will allow to approach the design process more efficiently and safe additional time to both the Designers's Community and our company. Thank you for understanding.
Clarification, please submit two variations of a design:
1) 1 page "business card" design that the company will be able to use during its startup stage;
2) the fully functional design (as per the requirements outlined below) for the company to transition to after the start-up period is over. Same design principles as developed for option 1 should be used for this variation.
Additional clarification, please note that the news block will not require images (at least during the start-up stage). It is envisioned to be a news feeder.
~ April 21, 2017 Update ~
Preliminary comments after receiving first designs:
- please try to create a unique design, using common elements wisely. Though such solar energy "attributes" as a solar panel or a bulb are very well recognized and allow quickly identify the nature of the business, they also became so common that in many cases a design may seem very similar to the one of others (Oh!, I've already seen this... effect).
- please try to introduce the company's logo unobtrusively. The size and position of the logo should clearly identify the company, but the message should be subtle, the logo should not distract from the main design. Brask's swoosh did not need to occupy have the screen.
- please use the green color with caution as it was with the company's logo. True, it is a green energy. But there is no need for the color to "scream" about it. Use the amount of green and its tone (avoid acid green) wisely.
--------------------------------------------------------------------------------
1. Main Goal
Develop a website that can represent the company to the industry stakeholders and become its "business card" during the start-up stage.
2. Secondary Goal
Develop a structure of a fully functional website that the "business card" design can eventually be transformed to staying consistent with the original design principles.
3. Key Audience
Varolu Corp. is providing consulting and technical services in the area of Solar Energy. The industry stakeholders include project developers, financial community, governmental bodies, OEMs, and competition.
4. Site Map
- HOME
• About
• Services
• Solar Energy
• News
• Contacts
• Social Media
- SERVICES*
- PROJECTS*
- FINANCE*
- TRAINING*
- SOLAR (ENERGY)*
* Maybe inactive / partially functional during the start-up stage.
5. Technical Specifications
Online brochure website during the start-up stage with a capability to be eventually transformed to a fully functional website while preserving the original design principles.
The design to be appealing, "light", professional, and with an intuitive and easy to navigate interface. Modern coding principles supporting efficiency and security to be utilized. Newest industry trends in website coding will be welcome.
The website to be designed so that it would fit well a computer, tablet, or mobile phone screen of any size. Cross-platform functionality to be taken into consideration to ensure that the website is fully functional on any platform.
Company's logo has already been designed and will be shared with the short-listed designers during the final design stage.
6. Interaction
The website will provide information about the company, our services, and projects. In addition, the industry insight, accumulated knowledge, and most recent trends are planned to be shared with stakeholders and attract and retain the audience.
Interaction with designers during the website development is envisioned to go through the following steps:
a) conceptual design - to be proposed by a designer originally. All conceptual designs will be reviewed and a feedback provided to pre-selected designers;
b) (preliminary and) final design - depending on the level of additional changes required can be broken into two steps. After discussing preliminary designs, company images will be provided to the selected finalists, who will compete with their final proposals.
7. Industry Stakeholders
- https://www.quellbrin.com/power/solar-power.- http://www.pakortavon.com/
- http://www.vellitrazo.com/about/company/
- https://www.oruxem.com/energy/index.html
8. Budget
Defined by the project.
9. Timescale
Defined by the project.
12. Additional Info
- No copy-cats, standard graphics, or cliches please!
- Additional information / clarifications will be gladly provided upon request.
- This specification may be updated throughout the project to reflect discussions with / changes proposed by the Designers community.

```html
<!DOCTYPE html>
<html lang="en">
<head>
<meta charset="utf-8">
<title>Varolu Corp. — Start Up Page</title>
<link rel="stylesheet" href="https://fonts.googleapis.com/css2?family=Roboto:wght@400;500;700&display=swap">
<style>
  :root {
    --sky-top: #7f7d8a;
    --sky-mid: #a59a98;
    --haze: #c7a584;
    --hills: #6f6a52;
    --meadow: #5f7a2c;
    --meadow-dark: #45601c;
    --white: #ffffff;
    --frame: rgba(255, 255, 255, 0.55);
    --accent: #e8900a;
    --logo-dot: #f3a712;
  }
  * { margin: 0; padding: 0; box-sizing: border-box; }
  html, body {
    width: 1200px;
    height: 729px;
    overflow: hidden;
  }
  body {
    font-family: "Roboto", Arial, sans-serif;
    color: var(--white);
    position: relative;
  }
  .hero-backdrop {
    position: absolute;
    inset: 0;
    background:
      linear-gradient(180deg,
        var(--sky-top) 0%,
        var(--sky-mid) 30%,
        var(--haze) 62%,
        var(--hills) 72%,
        var(--meadow) 84%,
        var(--meadow-dark) 100%);
  }
  .hero-backdrop::after {
    content: "";
    position: absolute;
    inset: 0;
    background: rgba(40, 36, 40, 0.18);
  }
  .site-header {
    position: absolute;
    top: 0; left: 0; right: 0;
    height: 140px;
  }
  .brand {
    position: absolute;
    left: 89px;
    top: 52px;
    display: flex;
    align-items: center;
    gap: 12px;
    font-weight: 500;
    font-size: 34px;
    letter-spacing: 2px;
    color: var(--white);
    text-decoration: none;
  }
  .brand-dot {
    width: 64px;
    height: 64px;
    border-radius: 50%;
    background: var(--logo-dot);
    flex: none;
  }
  .menu-toggle {
    position: absolute;
    left: 1083px;
    top: 71px;
    width: 28px;
    height: 20px;
    display: block;
  }
  .intro {
    position: absolute;
    left: 0; right: 0;
    top: 283px;
    display: flex;
    flex-direction: column;
    align-items: center;
  }
  .intro-frame {
    width: 506px;
    height: 96px;
    border: 1px solid var(--frame);
    padding: 4px;
  }
  .intro-frame-inner {
    width: 100%;
    height: 100%;
    border: 1px solid var(--frame);
    display: flex;
    align-items: center;
    justify-content: center;
  }
  .intro-title {
    font-weight: 500;
    font-size: 61px;
    line-height: 1;
    letter-spacing: 0.5px;
  }
  .intro-tagline {
    margin-top: 17px;
    font-weight: 400;
    font-size: 38px;
    line-height: 1.1;
  }
  .cta {
    margin-top: 16px;
    width: 130px;
    height: 42px;
    background: var(--accent);
    color: var(--white);
    font-weight: 500;
    font-size: 14.5px;
    display: flex;
    align-items: center;
    justify-content: center;
    text-decoration: none;
    border-radius: 2px;
  }
  .site-footer {
    position: absolute;
    left: 0; right: 0;
    top: 696px;
    text-align: center;
    font-size: 13px;
    font-weight: 400;
  }
</style>
</head>
<body>
  <div class="hero-backdrop" role="img" aria-label="Landscape photo at sunset: green hillside, valley and mountains, with a tall white wind turbine on the right"></div>

  <header class="site-header">
    <a class="brand" href="#">
      <span class="brand-dot"></span>
      <span class="brand-name">VAROLU CORP.</span>
    </a>
    <svg class="menu-toggle" viewBox="0 0 28 20" aria-label="Menu">
      <rect x="0" y="0" width="28" height="2" fill="#ffffff"/>
      <rect x="0" y="9" width="28" height="2" fill="#ffffff"/>
      <rect x="0" y="18" width="28" height="2" fill="#ffffff"/>
    </svg>
  </header>

  <main class="intro">
    <div class="intro-frame">
      <div class="intro-frame-inner">
        <h1 class="intro-title">START UP PAGE</h1>
      </div>
    </div>
    <p class="intro-tagline">Solar Power Equipments &amp; Latest Products</p>
    <a class="cta" href="#">GET STARTED</a>
  </main>

  <footer class="site-footer">Copy Right 2017. All Rights Reserved</footer>
</body>
</html>
```